Korimet Business Cards

Korimet is a software startup and we are looking for business cards that help convey our employee personalities, as well as the professionalism of the company.
Our company font is Comfortaa - and the company logo is attached (we are okay having the text beside the logo if applicable) where we can find the company colour scheme. Cards can be horizontal or vertical format.
We are looking for a two sided business card - on the front we will see the personal details of the employee (name, position, email and phone number), and then on the back, we will see the business details (name and logo, address, phone number, website, email, company tagline: "Building Bold Software Ideas for the Modern Mobility World")
We want the design to be clean and simple, but also fun, modern, and capturing of a young startup vibe.

```html
<!DOCTYPE html>
<html lang="en">
<head>
<meta charset="utf-8">
<title>Korimet Business Cards</title>
<link href="https://fonts.googleapis.com/css2?family=Comfortaa:wght@400;600;700&display=swap" rel="stylesheet">
<style>
  :root{
    --page:#c9cbcd;
    --night:#0f1026;
    --violet:#5a4fa6;
    --violet-band:#544aa3;
    --coral:#e85d6a;
    --ink:#1d1d28;
    --white:#ffffff;
  }
  *{box-sizing:border-box;margin:0;padding:0}
  html,body{width:1200px;height:928px;overflow:hidden}
  body{background:var(--page);font-family:"Comfortaa",sans-serif;position:relative}
  .card{position:absolute;border-radius:18px;overflow:hidden}
  .card-back{left:267px;top:59px;width:670px;height:382px;background:var(--night)}
  .card-front{left:264px;top:484px;width:676px;height:386px;background:var(--white)}
  .orb{position:absolute;border-radius:50%}
  .back-orb-1{left:25px;top:21px;width:40px;height:40px;background:radial-gradient(circle at 30% 25%,#5a3f7a,#1a1530 80%)}
  .back-orb-2{left:538px;top:22px;width:104px;height:104px;background:radial-gradient(circle at 35% 20%,#6a4a8e,#1c1633 85%)}
  .back-orb-3{left:27px;top:141px;width:100px;height:100px;background:radial-gradient(circle at 40% 20%,#3a3a48,#0f1026 85%)}
  .back-orb-4{left:600px;top:203px;width:42px;height:42px;background:radial-gradient(circle at 35% 25%,#34343f,#0f1026 85%)}
  .brand-dot{position:absolute;border-radius:50%;background:var(--violet)}
  .brand-name{position:absolute;color:var(--violet);font-weight:700;letter-spacing:1px;text-align:center}
  .back-brand-dot{left:307px;top:80px;width:56px;height:56px}
  .back-brand-name{left:0;width:670px;top:150px;font-size:52px;line-height:1}
  .tagline{position:absolute;left:0;width:670px;top:254px;text-align:center;color:var(--white);font-size:16.5px;letter-spacing:.3px}
  .contact-band{position:absolute;left:0;top:285px;width:670px;height:97px;background:linear-gradient(180deg,var(--violet-band),#5b51a9);border-top:3px solid var(--coral);color:var(--white);font-size:16px;letter-spacing:.6px}
  .band-row{position:absolute;left:0;width:670px;display:flex;justify-content:center;gap:30px;align-items:center}
  .band-row.top{top:13px}
  .band-row.bottom{top:42px}
  .item{display:flex;align-items:center;gap:6px;white-space:nowrap}
  .icon{width:15px;height:15px;flex:none}
  .front-orb-1{left:23px;top:23px;width:46px;height:46px;background:linear-gradient(200deg,#86d4f2,#7fd6c8)}
  .front-orb-2{left:565px;top:23px;width:86px;height:86px;background:linear-gradient(225deg,#f3805d,#fde6dc 90%)}
  .front-orb-3{left:23px;top:254px;width:104px;height:104px;background:linear-gradient(45deg,#ffffff 10%,#9fc9ef 70%)}
  .front-orb-4{left:611px;top:319px;width:40px;height:40px;background:linear-gradient(45deg,#7b63c2,#d175b6)}
  .front-brand-dot{left:192px;top:140px;width:64px;height:64px}
  .front-brand-name{left:130px;width:190px;top:222px;font-size:42px;line-height:1}
  .divider-thin{position:absolute;left:337px;top:116px;width:1.5px;height:154px;background:var(--coral)}
  .divider-thick{position:absolute;left:335px;top:153px;width:5px;height:80px;background:var(--violet)}
  .person{position:absolute;left:366px;top:116px}
  .person-name{color:var(--violet);font-weight:700;font-size:29px;letter-spacing:.8px}
  .person-role{color:var(--ink);font-size:17px;margin-top:6px;letter-spacing:.4px}
  .person-contacts{list-style:none;margin-top:12px;color:var(--ink);font-size:17px;letter-spacing:.6px}
  .person-contacts li{display:flex;align-items:center;gap:6px;height:29px}
</style>
</head>
<body>

<section class="card card-back">
  <span class="orb back-orb-1"></span>
  <span class="orb back-orb-2"></span>
  <span class="orb back-orb-3"></span>
  <span class="orb back-orb-4"></span>
  <span class="brand-dot back-brand-dot"></span>
  <div class="brand-name back-brand-name">korimet</div>
  <p class="tagline">Building Bold Software Ideas for the Modern Mobility World</p>
  <div class="contact-band">
    <div class="band-row top">
      <span class="item">
        <svg class="icon" viewBox="0 0 16 16"><circle cx="8" cy="8" r="8" fill="#e85d6a"/><path d="M5 4.2l1.6-.3.8 2-1 .8a5 5 0 0 0 2.9 2.9l.8-1 2 .8-.3 1.6c-3.6.3-7.1-3.2-6.8-6.8z" fill="#fff"/></svg>
        1-844-555-0142
      </span>
      <span class="item">
        <svg class="icon" viewBox="0 0 16 16"><circle cx="8" cy="8" r="8" fill="#e85d6a"/><rect x="4" y="5" width="8" height="6" rx="1" fill="#fff"/><path d="M4.3 5.4L8 8.4l3.7-3" stroke="#e85d6a" fill="none" stroke-width="1"/></svg>
        info@korimet.ai
      </span>
      <span class="item">
        <svg class="icon" viewBox="0 0 16 16"><circle cx="8" cy="8" r="8" fill="#e85d6a"/><circle cx="8" cy="8" r="4.5" fill="none" stroke="#fff" stroke-width="1.2"/><path d="M3.5 8h9M8 3.5c-2 2.5-2 6.5 0 9M8 3.5c2 2.5 2 6.5 0 9" stroke="#fff" fill="none" stroke-width="1"/></svg>
        www.korimet.ai
      </span>
    </div>
    <div class="band-row bottom">
      <span class="item">
        <svg class="icon" viewBox="0 0 16 16"><path d="M8 1a5 5 0 0 1 5 5c0 3.7-5 9-5 9S3 9.7 3 6a5 5 0 0 1 5-5z" fill="#e85d6a"/><circle cx="8" cy="6" r="2" fill="#fff"/></svg>
        Suite 210, 88 Maple Ave, Waterloo, ON N2J 4K1
      </span>
    </div>
  </div>
</section>

<section class="card card-front">
  <span class="orb front-orb-1"></span>
  <span class="orb front-orb-2"></span>
  <span class="orb front-orb-3"></span>
  <span class="orb front-orb-4"></span>
  <span class="brand-dot front-brand-dot"></span>
  <div class="brand-name front-brand-name">korimet</div>
  <span class="divider-thin"></span>
  <span class="divider-thick"></span>
  <div class="person">
    <h1 class="person-name">Mara Quinlan</h1>
    <p class="person-role">Director</p>
    <ul class="person-contacts">
      <li>
        <svg class="icon" viewBox="0 0 16 16"><circle cx="8" cy="8" r="8" fill="#e85d6a"/><path d="M5 4.2l1.6-.3.8 2-1 .8a5 5 0 0 0 2.9 2.9l.8-1 2 .8-.3 1.6c-3.6.3-7.1-3.2-6.8-6.8z" fill="#fff"/></svg>
        1-844-555-0142
      </li>
      <li>
        <svg class="icon" viewBox="0 0 16 16"><circle cx="8" cy="8" r="8" fill="#e85d6a"/><rect x="4" y="5" width="8" height="6" rx="1" fill="#fff"/><path d="M4.3 5.4L8 8.4l3.7-3" stroke="#e85d6a" fill="none" stroke-width="1"/></svg>
        info@korimet.ai
      </li>
      <li>
        <svg class="icon" viewBox="0 0 16 16"><circle cx="8" cy="8" r="8" fill="#e85d6a"/><circle cx="8" cy="8" r="4.5" fill="none" stroke="#fff" stroke-width="1.2"/><path d="M3.5 8h9M8 3.5c-2 2.5-2 6.5 0 9M8 3.5c2 2.5 2 6.5 0 9" stroke="#fff" fill="none" stroke-width="1"/></svg>
        www.korimet.ai
      </li>
    </ul>
  </div>
</section>

</body>
</html>
```